Surviving Domestic Violence Flyer

I need a flyer that "POPS" to attract participants for my research project. I have added the important information on my draft flyer.

```html
<!DOCTYPE html>
<html lang="en">
<head>
<meta charset="utf-8">
<title>Request for Study Participants</title>
<link rel="stylesheet" href="https://fonts.googleapis.com/css2?family=Oswald:wght@600;700&family=Noto+Serif:wght@700;900&family=Source+Sans+3:wght@400;700&display=swap">
<style>
  :root {
    --page: #ffffff;
    --pink: #ec1f8d;
    --pink-soft: #f04a9f;
    --maroon: #4a0222;
    --maroon-deep: #3a0019;
    --yellow: #ffee00;
    --gold-text: #fff200;
    --teal: #3ec1bb;
    --teal-dark: #0d6d6a;
    --ink: #3c0a1f;
    --cream: #fffbe8;
    --butter: #fff27a;
    --white: #ffffff;
  }
  * { margin: 0; padding: 0; box-sizing: border-box; }
  html, body { width: 1200px; height: 900px; overflow: hidden; background: var(--page); }
  .canvas { position: relative; width: 1200px; height: 900px; }
  .flyer {
    position: absolute; left: 297px; top: 56px; width: 612px; height: 792px;
    background: var(--pink); overflow: hidden;
  }
  .title-band {
    position: absolute; left: 0; top: 46px; width: 612px; height: 126px;
    background: linear-gradient(180deg, var(--maroon-deep), var(--maroon) 70%, #5e0530);
    text-align: center; color: var(--white);
    font-family: "Oswald", "Arial Narrow", sans-serif; font-weight: 700;
    text-shadow: 3px 3px 0 rgba(0,0,0,.55);
  }
  .title-band .line-one { position: absolute; left: 0; right: 0; top: 6px; font-size: 50px; line-height: 60px; }
  .title-band .line-two { position: absolute; left: 0; right: 0; top: 60px; font-size: 58px; line-height: 66px; }
  .topic-area { position: absolute; left: 0; top: 172px; width: 612px; height: 442px; }
  .topic-texture {
    position: absolute; inset: 0;
    background:
      radial-gradient(circle at 75% 20%, rgba(255,255,255,.18), transparent 35%),
      radial-gradient(circle at 20% 60%, rgba(200,0,110,.35), transparent 40%),
      radial-gradient(circle at 90% 70%, rgba(200,0,110,.35), transparent 30%),
      linear-gradient(180deg, var(--pink-soft), var(--pink));
  }
  .rule { position: absolute; left: 0; width: 612px; height: 1px; background: var(--yellow); }
  .rule.upper { top: 20px; }
  .rule.lower { top: 184px; }
  .tab { position: absolute; top: 25px; width: 29px; height: 157px; background: linear-gradient(90deg, var(--teal-dark), var(--teal) 60%, #7fd8d2); }
  .tab.left { left: 0; border-radius: 0 8px 8px 0; }
  .tab.right { right: 0; border-radius: 8px 0 0 8px; transform: scaleX(-1); }
  .topic-title {
    position: absolute; left: 0; right: 0; top: 28px; text-align: center;
    font-family: "Noto Serif", Georgia, serif; font-weight: 900; font-size: 31px; line-height: 38.5px;
    color: var(--gold-text);
    text-shadow: 1px 1px 0 #6b0a35, -1px -1px 0 #6b0a35, 1px -1px 0 #6b0a35, -1px 1px 0 #6b0a35, 3px 3px 3px rgba(60,0,25,.6);
  }
  .criteria-frame {
    position: absolute; left: 88px; top: 210px; width: 437px; height: 217px;
    border: 1.5px dashed rgba(255,255,255,.85); border-radius: 16px;
  }
  .criteria {
    position: absolute; left: 4px; top: 4px; right: 4px; bottom: 4px;
    border-radius: 13px;
    background: linear-gradient(180deg, var(--white) 5%, var(--cream) 35%, var(--butter));
    padding: 21px 8px 0 27px; list-style: none;
    font-family: "Source Sans 3", "Myriad Pro", Arial, sans-serif; font-size: 13px; color: var(--ink);
  }
  .criteria li { position: relative; padding-left: 21px; line-height: 27.6px; white-space: nowrap; }
  .criteria li::before {
    content: ""; position: absolute; left: 0; top: 8px; width: 12px; height: 12px;
    border-radius: 50%; background: var(--maroon);
  }
  .details {
    position: absolute; left: 0; top: 614px; width: 612px; height: 178px;
    background: linear-gradient(180deg, var(--maroon-deep) 0%, #6a0638 45%, var(--pink) 100%);
    font-family: "Source Sans 3", "Myriad Pro", Arial, sans-serif; font-size: 11.2px; line-height: 14.5px;
    color: var(--white); text-align: center; padding-top: 14px;
  }
  .details p { margin-bottom: 8px; }
  .details .highlight { color: var(--yellow); font-weight: 700; }
  .details .credits { margin-top: 13px; }
</style>
</head>
<body>
<div class="canvas">
  <section class="flyer">
    <header class="title-band">
      <h1>
        <span class="line-one">REQUEST For</span>
        <span class="line-two">STUDY PARTICIPANTS</span>
      </h1>
    </header>

    <div class="topic-area">
      <div class="topic-texture" role="img" aria-label="Soft pink abstract background with faint light circles"></div>
      <div class="rule upper"></div>
      <div class="rule lower"></div>
      <div class="tab left"></div>
      <div class="tab right"></div>
      <h2 class="topic-title">EFFICIENCY OF<br>RESOURCES AVAILABLE<br>TO SUVIVORS<br>OF INTIMATE PARTNER ABUSE</h2>

      <div class="criteria-frame">
        <ul class="criteria">
          <li>Are you eighteen years of age or older?</li>
          <li>Have you been a victim of domestic violence?</li>
          <li>Have you sought assistance with abuse in the last 12 months?</li>
          <li>Are you still in contact with the person who abuse you?</li>
          <li>Are you willing and open to discussing your experience with<br>abuse and your attemps to access services or resources?</li>
        </ul>
      </div>
    </div>

    <footer class="details">
      <p>If you answered yes to all of these questions, you may be eligible to participate in a study to better<br>understand the resources needed and services expected for survivors of domestic violence.</p>
      <p>Please contact <span class="highlight">Dana Whitfield</span> at <span class="highlight">1(555)014-2290</span> or via e-mail <span class="highlight">survivorstudy@example.org</span><br>for additional information</p>
      <p>Participants will be compensated for their time</p>
      <div class="credits">
        Principal Investigator : <span class="highlight">Dana Whitfield</span><br>
        Institutional Affliation : Lakeshore State University, Dept. of Criminology, Law, and Justice<br>
        Contact Address : Post Office Box 20418, Riverton, IL, 60000
      </div>
    </footer>
  </section>
</div>
</body>
</html>
```